Political Magazine & Corresponding Magazine Logo

I need a design for a monthly e-magazine that focuses on politics, public policy, as well as social, environmental, and economic justice. I would like a vibrant front and back cover, as well as internal pages that include a variety of design elements.

This magazine will be electronic ONLY and will not be published in print at this time.

I also need a logo design for the magazine that is attractive, includes the colors and images that communicate "authority" "trusted source", "professional", etc.

Industry/Entity Type

Political

Logo Text

Harborline Ember Review

Font styles to use
Serif
Sans Serif

Colors

Designer to choose colors to be used in the design.

Requirements
Must have
• I want the magazine design to include a variety of design elements that are consistent with the logo, as well as callouts, space for images, etc.
• I also need a logo design for the magazine that is attractive, includes the colors and images that communicate "authority" "trusted source", "professional", etc.
• I would like to have a color logo AND a white & black version of the same logo.
Nice to have
• I like various shades of navy blue.

```html
<!DOCTYPE html>
<html lang="en">
<head>
<meta charset="utf-8">
<title>Harborline Ember Review — Cover</title>
<link href="https://fonts.googleapis.com/css2?family=Playfair+Display:ital,wght@0,400;0,700;0,900;1,700;1,900&display=swap" rel="stylesheet">
<style>
  :root {
    --backdrop: #5d6167;
    --navy: #0f2340;
    --navy-deep: #0b1630;
    --ink: #0a0a0b;
    --paper: #f3f3f6;
    --gold: #a8976a;
    --gold-faint: #5c5440;
    --white: #ffffff;
    --teaser-ink: #1b2540;
  }
  * { box-sizing: border-box; margin: 0; padding: 0; }
  html, body { width: 1200px; height: 1200px; overflow: hidden; }
  body {
    background: var(--backdrop);
    font-family: "Playfair Display", Georgia, serif;
    display: flex; align-items: center; justify-content: center;
  }
  .cover {
    position: relative;
    width: 840px; height: 1120px;
    background: var(--ink);
    border: 8px solid var(--navy);
    overflow: hidden;
  }
  .teaser-band {
    position: absolute; left: 0; top: 0; right: 0; height: 180px;
    background: var(--paper);
    display: flex; justify-content: space-around; align-items: center;
    padding: 0 18px;
  }
  .teaser { display: flex; gap: 10px; align-items: center; }
  .teaser-text {
    color: var(--teaser-ink); font-weight: 900; font-size: 17px;
    line-height: 1.12; text-transform: uppercase; width: 150px;
  }
  .teaser-page { display: block; margin-top: 10px; font-weight: 400; font-size: 12px; color: #7a7f8c; text-transform: none; }
  .teaser-thumb { width: 78px; height: 108px; flex: none; }
  .thumb-a { background: linear-gradient(160deg, #8a8580, #2c2a28); }
  .thumb-b { background: linear-gradient(160deg, #efe6d8, #b9a78e 60%, #2a2a2e); }
  .thumb-c { background: linear-gradient(180deg, #d9dadc, #7d7568); }
  .cover-photo {
    position: absolute; left: 300px; top: 250px; right: 0; bottom: 0;
    background:
      radial-gradient(ellipse 45% 38% at 55% 40%, #d98a5e 0%, #b0603c 45%, rgba(20,12,10,0) 100%),
      radial-gradient(ellipse 30% 25% at 70% 92%, #c0272d 0%, rgba(192,39,45,0) 100%),
      linear-gradient(180deg, #0a0a0b, #141210);
  }
  .masthead { position: absolute; left: 0; right: 0; top: 196px; text-align: center; }
  .masthead-top {
    color: var(--gold); font-weight: 900; font-size: 66px; letter-spacing: 0.5px;
    line-height: 1; text-transform: uppercase;
  }
  .masthead-rule { width: 690px; height: 1px; background: var(--gold); margin: 10px auto 0; }
  .masthead-main {
    color: var(--white); font-weight: 900; font-size: 190px; line-height: 0.95;
    text-transform: uppercase; letter-spacing: -2px;
  }
  .issue-line {
    position: absolute; left: 96px; top: 480px;
    color: var(--gold); font-size: 17px;
  }
  .cover-lines { position: absolute; left: 56px; top: 560px; }
  .cover-line { position: relative; padding: 0 0 0 18px; margin-bottom: 44px; }
  .cover-line-num {
    position: absolute; left: -6px; top: -14px;
    font-weight: 900; font-size: 110px; line-height: 1; color: var(--gold-faint);
  }
  .cover-line-text {
    position: relative; color: var(--gold); font-weight: 900; font-size: 27px;
    line-height: 1.15; text-transform: uppercase;
  }
  .lead-headline {
    position: absolute; left: 120px; top: 790px;
    color: var(--white); font-weight: 700; font-size: 74px; line-height: 1.02;
    letter-spacing: -0.5px;
  }
  .pull-quote {
    position: absolute; right: 20px; bottom: 150px;
    width: 230px; height: 230px; border-radius: 50%;
    background: var(--navy-deep);
    display: flex; flex-direction: column; align-items: center; justify-content: center;
    text-align: center; padding: 30px;
    font-style: italic; font-weight: 700; font-size: 19px; line-height: 1.2; color: var(--white);
  }
  .pull-quote-name { color: var(--gold); font-weight: 900; text-transform: uppercase; font-size: 18px; }
</style>
</head>
<body>
  <main class="cover">
    <div class="cover-photo" role="img" aria-label="Cover portrait of a smiling politician in a dark suit and red tie"></div>

    <header class="teaser-band">
      <article class="teaser">
        <p class="teaser-text">Net velitat blation sequo oruptatiae. quiae officit<span class="teaser-page">Page 2</span></p>
        <div class="teaser-thumb thumb-a" role="img" aria-label="Portrait of an older man in a knit cap"></div>
      </article>
      <article class="teaser">
        <p class="teaser-text">Net velitat blation sequo oruptatiae. quiae officit<span class="teaser-page">Page 3</span></p>
        <div class="teaser-thumb thumb-b" role="img" aria-label="Portrait of a young woman with blonde hair"></div>
      </article>
      <article class="teaser">
        <p class="teaser-text">Net velitat blation sequo oruptatiae. quiae officit<span class="teaser-page">Page 4</span></p>
        <div class="teaser-thumb thumb-c" role="img" aria-label="Figure standing over a ruined city"></div>
      </article>
    </header>

    <div class="masthead">
      <div class="masthead-top">Harborline Ember</div>
      <div class="masthead-rule"></div>
      <div class="masthead-main">Review</div>
    </div>
    <p class="issue-line">Issue 2156 | June 2017</p>

    <section class="cover-lines">
      <div class="cover-line">
        <span class="cover-line-num">3</span>
        <p class="cover-line-text">Net velitat<br>blation sequo<br>oruptatiae</p>
      </div>
      <div class="cover-line">
        <span class="cover-line-num">17</span>
        <p class="cover-line-text">Net velitat<br>blation sequo<br>oruptatiae</p>
      </div>
    </section>

    <h1 class="lead-headline">net velitat<br>blation sequo<br>o Ruptatiae.<br>quiae officit</h1>

    <aside class="pull-quote">
      <span class="pull-quote-name">Halversen:</span>
      This is something like a quote and somewhere between five and 10 words
    </aside>
  </main>
</body>
</html>
```